Providing Back Office Solutions to Financial Advisors and Attorney Needs a Business Card Design

Need a Business Card Design that speaks to Financial Advisor and Attorneys. Some of the word that come to mind is Clean/Simple & Futuristic.

Industry/Entity Type

Business

```html
<!DOCTYPE html>
<html lang="en">
<head>
<meta charset="utf-8">
<title>Veridan Business Card</title>
<link href="https://fonts.googleapis.com/css2?family=Open+Sans:wght@400;600&display=swap" rel="stylesheet">
<style>
  :root {
    --stage: #2e2825;
    --card: #161616;
    --card-edge: #222222;
    --accent: #1f7fc0;
    --accent-soft: #2a8fd4;
    --ink: #f2f2f2;
    --muted: #8a8a8a;
    --mark: #3a3a3a;
  }
  * { margin: 0; padding: 0; box-sizing: border-box; }
  html, body { width: 1200px; height: 864px; overflow: hidden; }
  body {
    background: var(--stage);
    font-family: "Open Sans", Arial, sans-serif;
    display: flex;
    align-items: center;
    justify-content: center;
    gap: 40px;
  }
  .card {
    width: 540px;
    height: 310px;
    background: var(--card);
    border: 1px solid var(--card-edge);
    border-radius: 3px;
    box-shadow: 0 18px 40px rgba(0,0,0,.45);
    position: relative;
  }

  /* Back face */
  .card-back {
    display: flex;
    flex-direction: column;
    align-items: center;
    justify-content: center;
    gap: 22px;
  }
  .back-brand {
    display: flex;
    align-items: center;
    gap: 14px;
  }
  .brand-square-large {
    width: 44px; height: 44px;
    background: var(--mark);
  }
  .back-brand-name {
    font-size: 40px;
    font-weight: 600;
    letter-spacing: 4px;
    color: #5c5c5c;
  }
  .back-url {
    font-size: 14px;
    letter-spacing: 5px;
    color: var(--muted);
  }

  /* Front face */
  .card-front {
    display: flex;
    align-items: center;
    padding: 0 34px 0 28px;
  }
  .front-brand {
    display: flex;
    align-items: center;
    gap: 10px;
    width: 250px;
  }
  .brand-square {
    width: 30px; height: 30px;
    background: var(--accent);
    flex-shrink: 0;
  }
  .brand-divider {
    width: 1px;
    height: 52px;
    background: var(--accent);
  }
  .brand-words { display: flex; flex-direction: column; }
  .brand-name {
    font-size: 30px;
    font-weight: 600;
    letter-spacing: 2px;
    color: var(--accent-soft);
    line-height: 1;
  }
  .brand-tagline {
    font-size: 9.5px;
    font-weight: 600;
    letter-spacing: .5px;
    color: var(--accent);
    margin-top: 4px;
  }
  .front-details {
    margin-left: auto;
    color: var(--ink);
    font-size: 13px;
    line-height: 1.38;
  }
  .person-name {
    font-size: 16px;
    font-weight: 600;
    color: var(--accent-soft);
    letter-spacing: .5px;
  }
  .person-title {
    font-size: 12px;
    color: var(--accent);
    margin-bottom: 8px;
  }
  .address { margin-bottom: 4px; }
  .contact-list { list-style: none; }
  .contact-list li { display: flex; align-items: center; gap: 8px; }
  .contact-icon { width: 11px; height: 11px; fill: var(--accent); flex-shrink: 0; }
</style>
</head>
<body>

  <section class="card card-back" aria-label="Card back">
    <div class="back-brand">
      <span class="brand-square-large"></span>
      <span class="back-brand-name">VERIDAN</span>
    </div>
    <p class="back-url">www.veridan.com</p>
  </section>

  <section class="card card-front" aria-label="Card front">
    <div class="front-brand">
      <span class="brand-square"></span>
      <span class="brand-divider"></span>
      <div class="brand-words">
        <span class="brand-name">VERIDAN</span>
        <span class="brand-tagline">BACK OFFICE SOLUTIONS</span>
      </div>
    </div>

    <div class="front-details">
      <p class="person-name">MARK ELLISON</p>
      <p class="person-title">CEO/FOUNDER</p>
      <p class="address">1420 Harbor Row<br>Juneau, Alaska 99801</p>
      <ul class="contact-list">
        <li>
          <svg class="contact-icon" viewBox="0 0 12 12" aria-hidden="true"><path d="M1 3c0-1 1-2 2-2h1l1 3-1.5 1a6 6 0 0 0 2.5 2.5L7 6l3 1v1c0 1-1 2-2 2A7 7 0 0 1 1 3z"/></svg>
          555 201 4187
        </li>
        <li>
          <svg class="contact-icon" viewBox="0 0 12 12" aria-hidden="true"><rect x="3" y="0.5" width="6" height="11" rx="1"/></svg>
          555 730 2265
        </li>
        <li>
          <svg class="contact-icon" viewBox="0 0 12 12" aria-hidden="true"><rect x="1" y="4" width="10" height="7" rx="1"/><rect x="3" y="1" width="6" height="3"/></svg>
          555 614 0392
        </li>
        <li>
          <svg class="contact-icon" viewBox="0 0 12 12" aria-hidden="true"><path d="M1 3h10v7H1z M1 3l5 4 5-4"/></svg>
          mark@veridan.com
        </li>
        <li>
          <svg class="contact-icon" viewBox="0 0 12 12" aria-hidden="true"><circle cx="6" cy="6" r="5"/></svg>
          www.veridan.com
        </li>
      </ul>
    </div>
  </section>

</body>
</html>
```